A business card design for a dental office. We have Two doctors working here. We practice general de

I already have a logo designed for the office with the name and a slogan.
Now I need to create design for a business card using the same logo.
Details Needed on the front side of the card are :
Gregory L. Vanmerick, DDS
Daniel R Hoskett, DDS
418 Birchwood Lane
Portland, CT 06512
Phone : 860 555 0193
Fax : 860 555 0194
Website : WWW.BrightcrestDental.Com
Office hours by appointment
On the back side of the card need :
Appointment
Date....................Time...................
With....................................
If unable to keep your appointment, please give 24-48 hours notice in order to avoid broken appointment fee.

Industry/Entity Type

Dental Clinic

Contact Information for Business Card

Gregory L. Vanmerick, DDS
Daniel R Hoskett, DDS
418 Birchwood Lane
Portland, CT 06512
Phone : 860 555 0193
Fax : 860 555 0194
Appointment

Requirements
Must have
• Keep the Name and slogan on the logo on the front of the card. You can move them around the Logo and Name/Slogan of business (Vanmerick Family Dentistry/Bright care for every grin) as you wish to get a feel of the design.
• Gregory L. Vanmerick, DDS
• Daniel R Hoskett, DDS
• 418 Birchwood Lane
• Portland, CT 06512
• Phone : 860 555 0193
• Fax : 860 555 0194
• WWW.BrightcrestDental.Com
• Keep these three groups above as they are together now in different areas of the front side.
• On the back side of the card need :
• Appointment
• Date....................Time...................
• With....................................
• If unable to keep your appointment, please give 24-48 hours notice in order to avoid broken appointment fee.

```html
<!DOCTYPE html>
<html lang="en">
<head>
<meta charset="UTF-8">
<title>Vanmerick Family Dentistry – Business Card</title>
<link rel="stylesheet" href="https://fonts.googleapis.com/css2?family=Ubuntu:wght@400;500;700&display=swap">
<style>
  :root {
    --brand-red: #e5262f;
    --brand-blue: #0f56a4;
    --card-white: #ffffff;
    --backdrop: #eceae6;
    --dot-blue: #1d4f9c;
  }
  * { box-sizing: border-box; margin: 0; padding: 0; }
  html, body { width: 1200px; height: 900px; overflow: hidden; }
  body {
    background: var(--backdrop);
    font-family: "Ubuntu", sans-serif;
    position: relative;
  }
  .card {
    position: absolute;
    width: 700px;
    height: 400px;
    background: var(--card-white);
    box-shadow: 0 6px 18px rgba(0,0,0,0.18);
    overflow: hidden;
  }

  /* ---------- Appointment side ---------- */
  .card--appointment { left: 440px; top: 40px; }
  .practice-lockup {
    position: absolute; left: 170px; top: 30px;
    display: flex; align-items: center; gap: 18px;
  }
  .practice-lockup__disc {
    width: 90px; height: 90px; border-radius: 50%;
    background: var(--brand-blue);
  }
  .practice-lockup__name {
    color: var(--brand-blue); font-weight: 700;
    font-size: 20px; letter-spacing: 2.5px; text-transform: uppercase;
    margin-top: 40px;
  }
  .practice-slogan {
    position: absolute; left: 290px; top: 102px; width: 360px;
    display: flex; align-items: center; gap: 10px;
    color: var(--brand-red); font-size: 9px; letter-spacing: 2.5px;
    text-transform: uppercase; white-space: nowrap;
  }
  .practice-slogan::before, .practice-slogan::after {
    content: ""; flex: 1; height: 1px; background: var(--brand-red);
  }
  .appointment-title {
    position: absolute; left: 240px; top: 160px;
    color: var(--brand-red); font-weight: 700; font-size: 24px;
  }
  .appointment-field {
    position: absolute; display: flex; align-items: baseline; gap: 10px;
    color: var(--brand-red); font-weight: 700; font-size: 18px;
  }
  .appointment-field__line {
    display: inline-block; height: 2px;
    border-bottom: 3px dotted var(--dot-blue);
  }
  .field-date { left: 40px; top: 140px; }
  .field-date .appointment-field__line { width: 150px; }
  .field-with { left: 40px; top: 205px; }
  .field-with .appointment-field__line { width: 210px; }
  .field-time { left: 340px; top: 215px; }
  .field-time .appointment-field__line { width: 290px; }
  .field-with-cont {
    position: absolute; left: 90px; top: 258px; width: 500px;
    border-bottom: 3px dotted var(--dot-blue);
  }
  .cancellation-policy {
    position: absolute; left: 40px; right: 30px; top: 276px;
    font-weight: 700; font-size: 18px; line-height: 1.5;
  }
  .cancellation-policy__lead { color: var(--brand-red); }
  .cancellation-policy__tail { color: var(--brand-blue); padding-left: 40px; }

  /* ---------- Contact side ---------- */
  .card--contact { left: 60px; top: 470px; }
  .corner-mark { position: absolute; left: 0; top: 0; }
  .doctor-list { position: absolute; left: 96px; top: 26px; }
  .doctor-list__name { font-weight: 700; font-size: 21px; line-height: 1.3; }
  .doctor-list__name--first { color: var(--brand-red); }
  .doctor-list__name--second { color: var(--brand-blue); }
  .contact-block {
    position: absolute; left: 56px; top: 120px;
    color: var(--brand-blue); font-size: 18px; line-height: 1.3;
  }
  .contact-block__address { margin-bottom: 6px; padding-left: 20px; }
  .contact-line { display: flex; align-items: center; gap: 8px; }
  .contact-line svg { width: 13px; height: 13px; flex: none; }
  .contact-block__hours { margin-top: 2px; }
  .footer-bands { position: absolute; left: 0; bottom: 0; }
  .front-lockup {
    position: absolute; left: 420px; top: 70px; width: 250px;
    display: flex; flex-direction: column; align-items: center; gap: 14px;
  }
  .front-lockup__disc {
    width: 170px; height: 170px; border-radius: 50%;
    background: var(--brand-blue);
  }
  .front-lockup__name {
    color: var(--brand-blue); font-weight: 700; font-size: 16px;
    letter-spacing: 2px; text-transform: uppercase; text-align: center; line-height: 1.3;
  }
</style>
</head>
<body>

<section class="card card--appointment">
  <div class="practice-lockup">
    <div class="practice-lockup__disc"></div>
    <div class="practice-lockup__name">Vanmerick Family Dentistry</div>
  </div>
  <div class="practice-slogan">Bright care for every grin</div>

  <div class="appointment-field field-date">Date <span class="appointment-field__line"></span></div>
  <div class="appointment-title">Appointment</div>
  <div class="appointment-field field-with">With <span class="appointment-field__line"></span></div>
  <div class="appointment-field field-time">Time <span class="appointment-field__line"></span></div>
  <div class="field-with-cont"></div>

  <p class="cancellation-policy">
    <span class="cancellation-policy__lead">If unable to keep your appointment, please give 24-48 hours</span><br>
    <span class="cancellation-policy__tail">notice in order to avoid broken appointment fee.</span>
  </p>
</section>

<section class="card card--contact">
  <svg class="corner-mark" width="80" height="50" viewBox="0 0 80 50" aria-hidden="true">
    <polygon points="0,0 80,0 80,6 0,50" fill="var(--brand-red)"/>
    <polygon points="80,6 80,50 10,50" fill="var(--brand-blue)"/>
  </svg>

  <div class="doctor-list">
    <div class="doctor-list__name doctor-list__name--first">Gregory L. Vanmerick, DDS</div>
    <div class="doctor-list__name doctor-list__name--second">Daniel R Hoskett, DDS</div>
  </div>

  <div class="contact-block">
    <div class="contact-block__address">418 Birchwood Lane<br>Hollisford, CT 06512</div>
    <div class="contact-line">
      <svg viewBox="0 0 16 16" aria-label="Phone"><path d="M3 1l3 3-2 2c1 2 3 4 5 5l2-2 3 3-2 3C6 14 2 10 1 3z" fill="var(--brand-red)"/></svg>
      860 555 0193
    </div>
    <div class="contact-line">
      <svg viewBox="0 0 16 16" aria-label="Fax"><rect x="1" y="5" width="14" height="9" rx="1" fill="var(--brand-red)"/><rect x="4" y="1" width="8" height="5" fill="var(--brand-red)"/></svg>
      860 555 0194
    </div>
    <div class="contact-line">
      <svg viewBox="0 0 16 16" aria-label="Website"><circle cx="8" cy="8" r="7" fill="var(--brand-red)"/><path d="M1 8h14M8 1c3 3 3 11 0 14M8 1c-3 3-3 11 0 14" stroke="#fff" stroke-width="1.2" fill="none"/></svg>
      WWW.BrightcrestDental.Com
    </div>
    <div class="contact-block__hours">Office hours by appointment</div>
  </div>

  <div class="front-lockup">
    <div class="front-lockup__disc"></div>
    <div class="front-lockup__name">Vanmerick<br>Family Dentistry</div>
  </div>

  <svg class="footer-bands" width="700" height="90" viewBox="0 0 700 90" aria-hidden="true">
    <polygon points="0,0 300,48 300,62 0,14" fill="var(--brand-red)"/>
    <polygon points="300,48 700,48 700,90 290,90 310,62" fill="var(--brand-blue)"/>
  </svg>
</section>

</body>
</html>
```